Graphic Design/Logo Needed for Ear Drops Bottle

We have an Ear Drop Medication that we need to create a new label for. We will use a retro picture of a Doctor (Dr. Blenham) and the name of the product is Tidy Lobe. There is no official logo, so we will want to create a retro, basic logo for Tidy Lobe and use the retro picture. Front portion of the label is Size is 1.5" in height, and about 1.375" Width. this is a small tube similar in size to eye drops. We will be looking for just the logo portion and what you will see on the front of the bottle.

Target Market(s)

Medical Container

Industry/Entity Type

Medical

Font styles to use
Serif
Sans Serif

Colors
0054AA
0677BA
7BADD7
CADEEF
E8F1F8
FFF300
FFF600
FEFA6F
FFFEC7
FFFEE8

Requirements
Must have
• Picture of Dr. Blenham, "Tidy Lobe", Dr. Blenham's Ear Solution
Nice to have
• Retro Style or Modern with Retro Feel, Clean and engaging

```html
<!DOCTYPE html>
<html lang="en">
<head>
<meta charset="utf-8">
<title>Tidy Lobe – Dr. Blenham's Ear Solution label</title>
<link rel="stylesheet" href="https://fonts.googleapis.com/css2?family=Sniglet:wght@800&family=Mouse+Memoirs&display=swap">
<style>
  :root {
    --label-red: #da2f39;
    --ring-gold: #ebb53c;
    --cream: #f8f0d0;
    --skin: #f2c9a3;
    --shirt-blue: #6aa6cf;
    --coat-white: #e6f3f9;
    --coat-blue: #cfe6ef;
    --page: #ffffff;
    --ink-white: #ffffff;
  }
  * { margin: 0; padding: 0; box-sizing: border-box; }
  html, body {
    width: 1200px;
    height: 1198px;
    overflow: hidden;
    background: var(--page);
  }
  .sheet {
    position: relative;
    width: 1200px;
    height: 1198px;
  }

  /* Rectangular front label */
  .front-label {
    position: absolute;
    left: 323px;
    top: 104px;
    width: 555px;
    height: 509px;
    background: var(--label-red);
  }
  .front-label__stripes {
    position: absolute;
    left: 0;
    right: 0;
    top: 136px;
    height: 263px;
    background: repeating-linear-gradient(
      to bottom,
      var(--cream) 0 3px,
      var(--label-red) 3px 8.7px
    );
  }
  .front-label__name {
    position: absolute;
    left: 0;
    right: 14px;
    top: 20px;
    text-align: center;
    font-family: "Sniglet", "Arial Rounded MT Bold", sans-serif;
    font-weight: 800;
    font-size: 72px;
    line-height: 1;
    letter-spacing: 1px;
    color: var(--ink-white);
    text-transform: uppercase;
  }
  .front-label__tagline {
    position: absolute;
    left: 0;
    right: 0;
    top: 424px;
    text-align: center;
    font-family: "Mouse Memoirs", "Arial Narrow", sans-serif;
    font-size: 62px;
    line-height: 1;
    letter-spacing: 0.5px;
    color: var(--ink-white);
    text-transform: uppercase;
  }
  .front-label__portrait {
    position: absolute;
    left: 107px;
    top: 97px;
    width: 330px;
    height: 330px;
  }

  /* Round badge */
  .badge {
    position: absolute;
    left: 390px;
    top: 677px;
    width: 460px;
    height: 460px;
    filter: drop-shadow(8px 8px 6px rgba(0, 0, 0, 0.35));
  }
</style>
</head>
<body>
<main class="sheet">

  <section class="front-label">
    <div class="front-label__stripes"></div>
    <h1 class="front-label__name">Tidy Lobe</h1>

    <svg class="front-label__portrait" viewBox="0 0 330 330">
      <defs>
        <linearGradient id="portraitTone" x1="0" y1="0" x2="0" y2="1">
          <stop offset="0" stop-color="var(--cream)"/>
          <stop offset="0.2" stop-color="var(--cream)"/>
          <stop offset="0.45" stop-color="var(--skin)"/>
          <stop offset="0.62" stop-color="var(--shirt-blue)"/>
          <stop offset="0.78" stop-color="var(--coat-white)"/>
          <stop offset="1" stop-color="var(--coat-blue)"/>
        </linearGradient>
      </defs>
      <circle cx="165" cy="165" r="160" fill="var(--ring-gold)"/>
      <circle cx="165" cy="165" r="148" fill="url(#portraitTone)"
              role="img" aria-label="Retro illustration of Dr. Blenham in a white coat, blue shirt and head mirror"/>
    </svg>

    <p class="front-label__tagline">Dr. Blenham's Ear Solution</p>
  </section>

  <svg class="badge" viewBox="0 0 460 460">
    <defs>
      <linearGradient id="badgeTone" x1="0" y1="0" x2="0" y2="1">
        <stop offset="0" stop-color="var(--cream)"/>
        <stop offset="0.2" stop-color="var(--cream)"/>
        <stop offset="0.45" stop-color="var(--skin)"/>
        <stop offset="0.62" stop-color="var(--shirt-blue)"/>
        <stop offset="0.78" stop-color="var(--coat-white)"/>
        <stop offset="1" stop-color="var(--coat-blue)"/>
      </linearGradient>
    </defs>
    <circle cx="230" cy="230" r="229" fill="var(--ring-gold)"/>
    <circle cx="230" cy="230" r="212" fill="url(#badgeTone)"
            role="img" aria-label="Retro illustration of Dr. Blenham in a white coat, blue shirt and head mirror"/>
  </svg>

</main>
</body>
</html>
```